Bakery Replacement Lighted Sign Face

We are opening a new bakery that sells only cakes. The name is "The Willow Lantern." We are replacing the current sign face with a new look that states our name and makes a bold statement of fun. We will be known for having 101 cakes that are always ready for immediate pickup or delivery. Our colors are pink, orange, and lime green. An image is provided to see the colors.

Target Market(s)

people who buy cakes for parties and all other occasions

Industry/Entity Type

Cakes

Other font styles liked:
• look at the logo and file for the main font name

Colors
59FF00
82FF00
B8FF75
E3FFCB
F4FFEA
F0912C
F2A743
F7CA91
FBE8D2
FDF5EE
EB3D1F
EC4F4E
F09395
F8D3D4
FCEDEE

Requirements
Must have
• The name of the bakery. Logo can be used as is or changed as shown in one of the uploaded PDFs. Must use either pink, orange, lime green, white, or black. We prefer a bright pink background with white lettering as our first choice, but are willing to be open minded to see all creative concepts. Also the sign is 14 feet long and 42 inches tall so the artwork must fit within those boundaries. Also keep in mind the sign does have a 4 inch black frame. So the graphics area is actually 13 feet 2 inches by 3 feet. Also, in the attached pdf that shows a rough possible layout, the words "365 Slices To Go" is on the sign. It is NOT a must. Only use the wording if it adds to your design.
Nice to have
• You are welcome to add additional stars or other fun graphics that could look good.
Should not have
• No images of cakes or other bakery products.

```html
<!DOCTYPE html>
<html lang="en">
<head>
<meta charset="utf-8">
<title>The Willow Lantern – Sign Face Options</title>
<link rel="stylesheet" href="https://fonts.googleapis.com/css2?family=Fredoka:wght@600&family=Dosis:wght@700&display=swap">
<style>
  :root {
    --page: #ffffff;
    --pink: #ec5ba6;
    --plum: #522873;
    --lime: #5bf000;
    --coral: #f07b78;
    --white: #ffffff;
    --band: rgba(255, 255, 255, 0.35);
  }
  * { box-sizing: border-box; margin: 0; padding: 0; }
  html, body {
    width: 1136px;
    height: 1200px;
    overflow: hidden;
    background: var(--page);
  }
  .sheet {
    position: relative;
    width: 1136px;
    height: 1200px;
  }
  .sign {
    position: absolute;
    left: 46px;
    width: 1042px;
    height: 260px;
    overflow: hidden;
  }
  .sign--pink { background: var(--pink); --accent: var(--lime); }
  .sign--plum { background: var(--plum); --accent: var(--coral); }
  .sign--one { top: 34px; }
  .sign--two { top: 324px; }
  .sign--three { top: 614px; }
  .sign--four { top: 904px; }

  .sign__sky {
    position: absolute;
    inset: 0;
    width: 1042px;
    height: 260px;
  }
  .sign__edge {
    position: absolute;
    top: 14px;
    width: 18px;
    height: 232px;
    border-radius: 9px;
    background: var(--band);
  }
  .sign__edge--left { left: 16px; }
  .sign__edge--right { right: 16px; }

  .brand {
    position: absolute;
    top: 50%;
    transform: translate(-50%, -50%);
    font-family: "Fredoka", sans-serif;
    font-weight: 600;
    color: var(--accent);
    text-align: center;
    line-height: 1;
    white-space: nowrap;
  }
  .brand--centre { left: 500px; }
  .brand--side { left: 240px; }
  .brand__line { display: block; font-size: 76px; }
  .brand__line--second { font-size: 48px; letter-spacing: 8px; margin-top: 6px; }

  .tagline {
    position: absolute;
    left: 522px;
    top: 50%;
    transform: translateY(-50%);
    font-family: "Dosis", sans-serif;
    font-weight: 700;
    font-size: 56px;
    letter-spacing: -0.5px;
    color: var(--white);
    white-space: nowrap;
  }
  .tagline__accent { color: var(--accent); }
</style>
</head>
<body>
<svg width="0" height="0" style="position:absolute">
  <defs>
    <symbol id="star" viewBox="-10 -10 20 20">
      <path d="M0,-10 L2.6,-3.3 L9.5,-3.1 L4.1,1.3 L5.9,8.1 L0,4.2 L-5.9,8.1 L-4.1,1.3 L-9.5,-3.1 L-2.6,-3.3 Z" fill="#fff"/>
    </symbol>
    <symbol id="burst" viewBox="-14 -14 28 28">
      <path d="M0,-8 L2.1,-2.6 L7.6,-2.5 L3.3,1 L4.7,6.5 L0,3.4 L-4.7,6.5 L-3.3,1 L-7.6,-2.5 L-2.1,-2.6 Z" fill="#fff"/>
      <g stroke="#fff" stroke-width="1.6" stroke-linecap="round">
        <line x1="0" y1="-13" x2="0" y2="-10"/>
        <line x1="0" y1="10" x2="0" y2="13"/>
        <line x1="-13" y1="0" x2="-10" y2="0"/>
        <line x1="10" y1="0" x2="13" y2="0"/>
        <line x1="-9" y1="-9" x2="-7" y2="-7"/>
        <line x1="9" y1="9" x2="7" y2="7"/>
        <line x1="9" y1="-9" x2="7" y2="-7"/>
        <line x1="-9" y1="9" x2="-7" y2="7"/>
      </g>
    </symbol>
  </defs>
</svg>

<main class="sheet">

  <section class="sign sign--pink sign--one">
    <svg class="sign__sky" viewBox="0 0 1042 260" aria-hidden="true">
      <use href="#star" x="99" y="54" width="22" height="22"/>
      <use href="#burst" x="210" y="27" width="24" height="24"/>
      <use href="#star" x="163" y="177" width="14" height="14"/>
      <use href="#burst" x="68" y="198" width="38" height="38"/>
      <use href="#burst" x="274" y="193" width="28" height="28"/>
      <use href="#burst" x="767" y="45" width="26" height="26"/>
      <use href="#burst" x="896" y="18" width="34" height="34"/>
      <use href="#star" x="963" y="63" width="22" height="22"/>
      <use href="#star" x="857" y="110" width="30" height="30"/>
      <use href="#burst" x="778" y="193" width="28" height="28"/>
      <use href="#star" x="940" y="182" width="26" height="26"/>
    </svg>
    <div class="sign__edge sign__edge--left" role="img" aria-label="Wavy white line border"></div>
    <div class="sign__edge sign__edge--right" role="img" aria-label="Wavy white line border"></div>
    <h1 class="brand brand--centre">
      <span class="brand__line">The Willow</span>
      <span class="brand__line brand__line--second">LANTERN</span>
    </h1>
  </section>

  <section class="sign sign--pink sign--two">
    <svg class="sign__sky" viewBox="0 0 1042 260" aria-hidden="true">
      <use href="#star" x="612" y="51" width="22" height="22"/>
      <use href="#burst" x="767" y="45" width="26" height="26"/>
      <use href="#burst" x="896" y="18" width="34" height="34"/>
      <use href="#star" x="963" y="63" width="22" height="22"/>
      <use href="#star" x="677" y="185" width="13" height="13"/>
      <use href="#burst" x="818" y="178" width="46" height="46"/>
      <use href="#star" x="940" y="188" width="26" height="26"/>
    </svg>
    <div class="sign__edge sign__edge--right" role="img" aria-label="Wavy white line border"></div>
    <h2 class="brand brand--side">
      <span class="brand__line">The Willow</span>
      <span class="brand__line brand__line--second">LANTERN</span>
    </h2>
    <p class="tagline">365 SLICES <span class="tagline__accent">TO GO</span></p>
  </section>

  <section class="sign sign--plum sign--three">
    <svg class="sign__sky" viewBox="0 0 1042 260" aria-hidden="true">
      <use href="#star" x="99" y="54" width="22" height="22"/>
      <use href="#burst" x="210" y="27" width="24" height="24"/>
      <use href="#star" x="163" y="177" width="14" height="14"/>
      <use href="#burst" x="68" y="198" width="38" height="38"/>
      <use href="#burst" x="274" y="193" width="28" height="28"/>
      <use href="#burst" x="767" y="45" width="26" height="26"/>
      <use href="#burst" x="896" y="18" width="34" height="34"/>
      <use href="#star" x="963" y="63" width="22" height="22"/>
      <use href="#star" x="857" y="110" width="30" height="30"/>
      <use href="#burst" x="778" y="193" width="28" height="28"/>
      <use href="#star" x="940" y="182" width="26" height="26"/>
    </svg>
    <div class="sign__edge sign__edge--left" role="img" aria-label="Wavy white line border"></div>
    <div class="sign__edge sign__edge--right" role="img" aria-label="Wavy white line border"></div>
    <h2 class="brand brand--centre">
      <span class="brand__line">The Willow</span>
      <span class="brand__line brand__line--second">LANTERN</span>
    </h2>
  </section>

  <section class="sign sign--plum sign--four">
    <svg class="sign__sky" viewBox="0 0 1042 260" aria-hidden="true">
      <use href="#star" x="612" y="51" width="22" height="22"/>
      <use href="#burst" x="767" y="45" width="26" height="26"/>
      <use href="#burst" x="896" y="18" width="34" height="34"/>
      <use href="#star" x="963" y="63" width="22" height="22"/>
      <use href="#star" x="677" y="185" width="13" height="13"/>
      <use href="#burst" x="818" y="178" width="46" height="46"/>
      <use href="#star" x="940" y="188" width="26" height="26"/>
    </svg>
    <div class="sign__edge sign__edge--right" role="img" aria-label="Wavy white line border"></div>
    <h2 class="brand brand--side">
      <span class="brand__line">The Willow</span>
      <span class="brand__line brand__line--second">LANTERN</span>
    </h2>
    <p class="tagline">365 SLICES <span class="tagline__accent">TO GO</span></p>
  </section>

</main>
</body>
</html>
```